Business Card & Logo Design for a communications based company

I am looking for a business card and logo design for a communications based company.. We specialize in Fiber Optics
I have an image i would like to use towards the logo which i have uploaded. (Use of the image is totally up to you the designers)
Background color - Blue OR Black. (thats just my preference..Use of those colors are totally up to the designer)
Text -
Company Name - Brisa Networks LTD
Name - Marcel Dostiwana
Contact Number - (555) 417-2904
Adress - Palmview Heights
Company Motto - Stay Connected !
Services Offered
Fiber Optic Solutions
Full Networking Solutions
IP Surveillance Systems
Access Control Systems
Alarms
Industry/Entity Type
Communications
Contact Information for Business Card
Text -
Name - Marcel Dostiwana
Adress - Palmview Heights
Services Offered
Fiber Optic Solutions
Full Networking Solutions
IP Surveillance Systems
Access Control Systems
Alarms

```html
<!DOCTYPE html>
<html lang="en">
<head>
<meta charset="utf-8">
<title>Brisa Networks LTD – Business Card</title>
<link href="https://fonts.googleapis.com/css2?family=Arimo:wght@400;700&display=swap" rel="stylesheet">
<style>
  :root {
    --page-bg: #e9e6e1;
    --card-black: #050505;
    --card-edge: #1b1b1b;
    --text-white: #ffffff;
    --text-grey: #d4d4d4;
    --accent-blue: #2aa7e0;
    --globe-blue: #1c7fd0;
    --globe-deep: #0b3f86;
    --cable-grey: #7e7e7e;
  }
  * { box-sizing: border-box; margin: 0; padding: 0; }
  html, body { width: 1200px; height: 885px; overflow: hidden; }
  body {
    background: var(--page-bg);
    font-family: "Arimo", Arial, sans-serif;
    position: relative;
  }
  .card {
    position: absolute;
    top: 288px;
    width: 540px;
    height: 309px;
    background: var(--card-black);
    border: 1px solid var(--card-edge);
    border-radius: 3px;
    overflow: hidden;
    color: var(--text-white);
    box-shadow: 0 6px 18px rgba(0,0,0,.25);
  }
  .card--front { left: 40px; }
  .card--back { left: 620px; }

  /* Front */
  .front-title {
    position: absolute; left: 26px; top: 22px;
    font-size: 31px; font-weight: 700; letter-spacing: -0.3px;
  }
  .front-art {
    position: absolute; left: 0; bottom: 0; width: 300px; height: 230px;
    background:
      radial-gradient(circle at 30% 40%, rgba(255,255,255,.35), transparent 40%),
      radial-gradient(ellipse at 60% 20%, var(--cable-grey) 0%, transparent 45%),
      radial-gradient(circle at 28% 95%, var(--globe-blue) 0%, var(--globe-deep) 45%, transparent 70%);
  }
  .contact {
    position: absolute; left: 318px; top: 118px; width: 210px;
  }
  .contact-name { font-size: 20px; font-weight: 700; margin-bottom: 6px; }
  .contact-line { font-size: 14px; color: var(--text-grey); line-height: 1.45; }
  .contact-icons {
    position: absolute; right: 14px; top: 118px;
    display: flex; flex-direction: column; gap: 5px;
  }
  .contact-icon {
    width: 17px; height: 17px; background: var(--accent-blue);
    display: flex; align-items: center; justify-content: center;
  }
  .contact-email {
    position: absolute; left: 232px; top: 246px;
    font-size: 14px; color: var(--text-grey);
  }

  /* Back */
  .back-title {
    position: absolute; left: 150px; top: 30px;
    font-size: 27px; font-weight: 700; letter-spacing: -0.3px;
  }
  .services-heading {
    position: absolute; left: 58px; top: 90px;
    font-size: 21px; font-weight: 700;
  }
  .services-list {
    position: absolute; left: 34px; top: 124px; list-style: none;
  }
  .services-list li {
    font-size: 15px; color: var(--text-grey); line-height: 1.45;
    display: flex; align-items: center; gap: 14px;
  }
  .services-list li::before {
    content: ""; width: 7px; height: 7px; border-radius: 50%;
    background: var(--accent-blue); flex: none;
  }
  .back-art {
    position: absolute; left: 0; bottom: 0; width: 360px; height: 120px;
    background: radial-gradient(ellipse at 55% 90%, rgba(90,90,90,.35), transparent 65%);
  }
</style>
</head>
<body>
  <section class="card card--front">
    <div class="front-art" role="img" aria-label="Illustration of a fibre optic cable with coloured strands wrapped around a blue globe"></div>
    <h1 class="front-title">Brisa Networks LTD</h1>
    <div class="contact">
      <p class="contact-name">Marcel Dostiwana</p>
      <p class="contact-line">(555) 417-2904</p>
      <p class="contact-line">Palmview Heights</p>
    </div>
    <div class="contact-icons">
      <span class="contact-icon">
        <svg width="11" height="11" viewBox="0 0 24 24" aria-hidden="true"><path fill="#fff" d="M6.6 10.8a15 15 0 0 0 6.6 6.6l2.2-2.2c.3-.3.7-.4 1-.2 1.1.4 2.3.6 3.6.6.6 0 1 .4 1 1V20c0 .6-.4 1-1 1A17 17 0 0 1 3 4c0-.6.4-1 1-1h3.5c.6 0 1 .4 1 1 0 1.3.2 2.5.6 3.6.1.3 0 .7-.2 1z"/></svg>
      </span>
      <span class="contact-icon">
        <svg width="11" height="11" viewBox="0 0 24 24" aria-hidden="true"><path fill="#fff" d="M12 2a7 7 0 0 0-7 7c0 5 7 13 7 13s7-8 7-13a7 7 0 0 0-7-7zm0 9.5A2.5 2.5 0 1 1 12 6.5a2.5 2.5 0 0 1 0 5z"/></svg>
      </span>
      <span class="contact-icon">
        <svg width="11" height="11" viewBox="0 0 24 24" aria-hidden="true"><path fill="#fff" d="M3 5h18v14H3z M3 5l9 7 9-7" stroke="#2aa7e0" stroke-width="1.5"/></svg>
      </span>
    </div>
    <p class="contact-email">info@brisanetworks.net</p>
  </section>

  <section class="card card--back">
    <div class="back-art" role="img" aria-label="Faint image of a fibre optic cable end"></div>
    <h2 class="back-title">Brisa Networks LTD</h2>
    <h3 class="services-heading">Services Offered</h3>
    <ul class="services-list">
      <li>Fiber Optic Solutions</li>
      <li>Full Networking Solutions</li>
      <li>IP Surveillance Systems</li>
      <li>Access Control Systems</li>
      <li>Alarms</li>
    </ul>
  </section>
</body>
</html>
```